Brisk Hollow Builders Needs A Flyer

We need a flyer for our newest product "The Cedarlane Garden Workroom"

Here is some copy for the flyer:

1. More and more people everyday are working from home and finding it difficult to disconnect from home activities in order to focus on their work. They are also finding it very expensive to add on to their existing house for a quiet place. Our archatectually stunning, Cedarlane Garden Workroom is the answer. The office studio measures 16' wide and 10' deep. 160 Square feet of space.

Perfect for dozens of purposes. Home office, design studio, artist studio, home school office, reading room, craft studio, drafting room.

Features include:

- Steel Framing. 40-60% lighter then wood, higher strength to weight ratio, resistant to mold and fire and steel is the most recycled material on earth!
- Spray foam insulation. Cool in the summer and warm in the winter.
- HVAC Mini Split with wireless remote control and thermostat.
- 100% Off grid with enough solar and battery storage to run your entire office. No need to pay for an expensive electric installation.
- Flush fitting floor outlets to reduce wires.
- TV mount (Optional with pre-wired electric, HDMI, digital audio & Cat 6)
- Windows are tempered glass custom made by Morvik Glazing.
- Solar qualifies for a 26% tax credit. This is not a write-off rather it is a direct reduction on your tax obligation.
- Thousands of dollars less than adding onto your home.
- Custom color, siding, features available.

This beautiful back yard office is delivered 100% assembled and ready to enjoy on the day of delivery.

We ship nationwide from our factory in South Carolina. Give us a call anytime to speak to a designer and start your dream office today!

555-318-4027
info@BriskHollowBuilders.example

```html
<!DOCTYPE html>
<html lang="en">
<head>
<meta charset="utf-8">
<title>The Cedarlane Garden Workroom – Brisk Hollow Builders</title>
<link href="https://fonts.googleapis.com/css2?family=Montserrat:wght@400;500;600;700;800;900&display=swap" rel="stylesheet">
<style>
:root{
  --backdrop:#9dafb6;
  --paper:#ffffff;
  --green:#5ca343;
  --green-deep:#4f9139;
  --orange:#e9a524;
  --ink:#1c1c1c;
  --charcoal:#3a3d3f;
  --ring:#8a8a8a;
}
*{margin:0;padding:0;box-sizing:border-box}
html,body{width:941px;height:1200px;overflow:hidden}
body{background:var(--backdrop);font-family:"Montserrat",sans-serif;color:var(--ink);position:relative}
.flyer{position:absolute;left:38px;top:36px;width:860px;height:1113px;background:var(--paper);box-shadow:4px 5px 8px rgba(0,0,0,.35);overflow:hidden}
.hero-shapes{position:absolute;left:0;top:0;width:860px;height:600px}
.headline{position:absolute;left:37px;top:64px;width:350px;font-weight:900;font-size:45px;line-height:64px;letter-spacing:0;text-transform:uppercase;white-space:nowrap}
.headline .accent{color:var(--orange);display:block}
.headline .light{color:#fff;display:block}
.brand-badge{position:absolute;left:39px;top:350px;width:270px;height:270px;border-radius:50%;background:#fff;border:1.5px solid var(--ring);display:flex;flex-direction:column;align-items:center;justify-content:center;text-align:center}
.brand-name{font-weight:800;font-size:27px;line-height:30px;color:var(--orange);text-transform:uppercase;letter-spacing:.5px}
.model{position:absolute;width:164px;height:164px;border-radius:50%;border:3px dashed var(--green);display:flex;align-items:center;justify-content:center}
.model .disc{width:144px;height:144px;border-radius:50%;display:flex;align-items:center;justify-content:center;overflow:hidden}
.model .disc.green{background:var(--green)}
.model .disc.orange{background:var(--orange)}
.model .render{width:108px;height:70px;background:linear-gradient(180deg,#3b3e40 0 10%,#d9d2c4 10% 90%,#3b3e40 90%);border-radius:2px}
.model-one{left:316px;top:475px}
.model-two{left:482px;top:547px}
.model-three{left:661px;top:546px}
.intro{position:absolute;left:35px;top:639px;width:286px;font-size:9.6px;line-height:12px;text-align:justify}
.purposes{position:absolute;left:37px;top:735px;width:320px;font-size:17.3px;line-height:20.3px;font-weight:500}
.delivery{position:absolute;left:37px;top:833px;width:292px;font-size:16.2px;line-height:20.3px;font-weight:800;color:var(--green);text-transform:uppercase}
.call-box{position:absolute;left:36px;top:932px;width:307px;height:166px;background:var(--orange);padding:11px}
.call-box .inner{width:100%;height:100%;border:1px dashed #3a2a05;display:flex;flex-direction:column;align-items:center;justify-content:center;text-align:center;text-transform:uppercase}
.call-box .ship{font-size:13.6px;line-height:17px;font-weight:500}
.call-box .cta{font-size:24px;line-height:26px;font-weight:900;margin-top:10px}
.call-box .more{font-size:13.6px;line-height:17px;font-weight:500}
.features-tab{position:absolute;left:393px;top:729px;width:218px;height:27px}
.features-tab .label{position:absolute;left:12px;top:0;line-height:27px;font-size:16.5px;font-weight:800;color:#fff;letter-spacing:.3px}
.feature-list{position:absolute;left:393px;top:767px;width:432px;list-style:none}
.feature-list li{position:relative;padding-left:19px;font-size:9.9px;line-height:12px;margin-bottom:11.5px}
.feature-list li svg{position:absolute;left:0;top:-1px;width:13px;height:13px}
.contact-bar{position:absolute;left:343px;top:1055px;width:517px;height:43px;background:var(--green);display:flex;align-items:center;color:#fff;font-weight:700}
.contact-bar .phone{font-size:19px;padding:0 10px 0 12px}
.contact-bar .divider{width:2px;height:31px;background:#fff}
.contact-bar .email{font-size:16px;padding-left:10px;font-weight:600}
</style>
</head>
<body>
<main class="flyer">
  <svg class="hero-shapes" viewBox="0 0 860 600">
    <defs>
      <linearGradient id="greenWash" x1="0" y1="0" x2="0" y2="1">
        <stop offset="0" stop-color="#5fa548"/>
        <stop offset="1" stop-color="#4c8f37"/>
      </linearGradient>
    </defs>
    <path d="M0,0 H430 V400 C560,520 720,480 860,415 V458 C700,545 400,560 0,528 Z" fill="url(#greenWash)"/>
    <path d="M0,527 L70,531 L70,562 L0,557 Z" fill="var(--orange)"/>
    <path d="M348,430 C440,505 540,515 620,505 C720,492 800,455 860,424" fill="none" stroke="#fff" stroke-width="22"/>
    <path d="M348,430 C440,505 540,515 620,505 C720,492 800,455 860,424" fill="none" stroke="var(--orange)" stroke-width="9"/>
    <path role="img" aria-label="Photo of the garden workroom: dark steel studio with full-height glass walls, wood double doors and a furnished interior, set on a stone path under a blue sky"
      d="M404,0 C425,150 423,300 362,405 C430,470 520,490 600,480 C700,470 800,430 860,395 V0 Z"
      fill="#8fb3cf" stroke="#fff" stroke-width="8"/>
  </svg>

  <h1 class="headline">
    <span class="accent">The</span>
    <span class="accent">Cedarlane</span>
    <span class="light">Garden</span>
    <span class="light">Workroom</span>
  </h1>

  <div class="brand-badge">
    <span class="brand-name">Brisk Hollow<br>Builders</span>
  </div>

  <div class="model model-one"><div class="disc green"><div class="render" role="img" aria-label="Workroom seen from the front left corner"></div></div></div>
  <div class="model model-two"><div class="disc orange"><div class="render" role="img" aria-label="Workroom seen straight from the front"></div></div></div>
  <div class="model model-three"><div class="disc green"><div class="render" role="img" aria-label="Workroom seen from the front right corner"></div></div></div>

  <p class="intro">More and more people everyday are working from home and finding it difficult to disconnect from home activities in order to focus on their work. They are also finding it very expensive to add on to their existing house for a quiet place. Our archatectually stunning, Cedarlane Garden Workroom is the answer. The office studio measures 16' wide and 10' deep. 160 Square feet of space.</p>

  <p class="purposes">Perfect for dozens of purposes. Home office, design studio, artist studio, home school office, reading room, craft studio, drafting room.</p>

  <p class="delivery">This beautiful back yard office is delivered 100% as&shy;sembled and ready to enjoy on the day of delivery.</p>

  <div class="call-box">
    <div class="inner">
      <p class="ship">We ship nationwide from our<br>factory in South Carolina.</p>
      <p class="cta">Give us a call</p>
      <p class="more">Anytime to speak to<br>a designer and start your<br>dream office today!</p>
    </div>
  </div>

  <div class="features-tab">
    <svg width="218" height="27" viewBox="0 0 218 27" aria-hidden="true">
      <polygon points="0,0 172,0 180,27 0,27" fill="var(--green)"/>
      <polygon points="175,0 218,0 218,27 183,27" fill="var(--orange)"/>
    </svg>
    <span class="label">FEATURES</span>
  </div>

  <ul class="feature-list">
    <li><svg viewBox="0 0 13 13"><circle cx="6.5" cy="6.5" r="6.5" fill="#5ca343"/><path d="M3.5 6.8 L5.7 8.9 L9.6 4.4" fill="none" stroke="#fff" stroke-width="1.6"/></svg>Steel Framing. 40-60% lighter then wood, higher strength to weight ratio, resistant to mold and fire and steel is the most recycled material on earth!</li>
    <li><svg viewBox="0 0 13 13"><circle cx="6.5" cy="6.5" r="6.5" fill="#5ca343"/><path d="M3.5 6.8 L5.7 8.9 L9.6 4.4" fill="none" stroke="#fff" stroke-width="1.6"/></svg>Spray foam insulation. Cool in the summer and warm in the winter.</li>
    <li><svg viewBox="0 0 13 13"><circle cx="6.5" cy="6.5" r="6.5" fill="#5ca343"/><path d="M3.5 6.8 L5.7 8.9 L9.6 4.4" fill="none" stroke="#fff" stroke-width="1.6"/></svg>HVAC Mini Split with wireless remote control and thermostat.</li>
    <li><svg viewBox="0 0 13 13"><circle cx="6.5" cy="6.5" r="6.5" fill="#5ca343"/><path d="M3.5 6.8 L5.7 8.9 L9.6 4.4" fill="none" stroke="#fff" stroke-width="1.6"/></svg>100% Off grid with enough solar and battery storage to run your entire office. No need to pay for an expensive electric installation.</li>
    <li><svg viewBox="0 0 13 13"><circle cx="6.5" cy="6.5" r="6.5" fill="#5ca343"/><path d="M3.5 6.8 L5.7 8.9 L9.6 4.4" fill="none" stroke="#fff" stroke-width="1.6"/></svg>Flush fitting floor outlets to reduce wires.</li>
    <li><svg viewBox="0 0 13 13"><circle cx="6.5" cy="6.5" r="6.5" fill="#5ca343"/><path d="M3.5 6.8 L5.7 8.9 L9.6 4.4" fill="none" stroke="#fff" stroke-width="1.6"/></svg>TV mount (Optional with pre-wired electric, HDMI, digital audio &amp; Cat 6)</li>
    <li><svg viewBox="0 0 13 13"><circle cx="6.5" cy="6.5" r="6.5" fill="#5ca343"/><path d="M3.5 6.8 L5.7 8.9 L9.6 4.4" fill="none" stroke="#fff" stroke-width="1.6"/></svg>Windows are tempered glass custom made by Morvik Glazing.</li>
    <li><svg viewBox="0 0 13 13"><circle cx="6.5" cy="6.5" r="6.5" fill="#5ca343"/><path d="M3.5 6.8 L5.7 8.9 L9.6 4.4" fill="none" stroke="#fff" stroke-width="1.6"/></svg>Solar qualifies for a 26% tax credit. This is not a write-off rather it is a direct reduction on your tax obligation.</li>
    <li><svg viewBox="0 0 13 13"><circle cx="6.5" cy="6.5" r="6.5" fill="#5ca343"/><path d="M3.5 6.8 L5.7 8.9 L9.6 4.4" fill="none" stroke="#fff" stroke-width="1.6"/></svg>Thousands of dollars less than adding onto your home.</li>
    <li><svg viewBox="0 0 13 13"><circle cx="6.5" cy="6.5" r="6.5" fill="#5ca343"/><path d="M3.5 6.8 L5.7 8.9 L9.6 4.4" fill="none" stroke="#fff" stroke-width="1.6"/></svg>Custom color, siding, features available.</li>
  </ul>

  <div class="contact-bar">
    <span class="phone">555-318-4027</span>
    <span class="divider"></span>
    <span class="email">info@BriskHollowBuilders.example</span>
  </div>
</main>
</body>
</html>
```